Security and Technology Website - Bold and Confident, Something Unexpected

Brightfern Systems is launching its first website and we need a great design to bring our brand to life and generate DTC and B2B leads.

We have a good logo, but I am struggling with the creative vision to bring it all together. While our industry is Alarm Systems and Technology, we want to create a site that is more friendly and less 'typical' than your standard IT sites.

It Must:
1. Appeal to both men and women. The logo is a bit masculine, so the colors and icons must soften this.
2. Feel modern - we need to convey that we we use the latest technology.
3. Feel a bit high-end. We are not a budget solution.
4. Have a distinct iconography and photo treatment.
5. Feel layered - not just a series of stacked horizontal modules.

It Should Not:
1. Feel like your typical IT website.

Here are resources to get you started!
• Staging Site:
https://brightfern-systems.shopsite-demo.com/
Password: Maple

•Brand Guide: https://www.layoutboard-demo.com/design/QWRT5plmK2X/aB3cD4eF5gH6iJ7kL8mN9o/edit?utm_content=QWRT5plmK2X&utm_campaign=designshare&utm_medium=link2&utm_source=sharebutton

• Logo and Fonts and Photos: :https://files.cloudvault-demo.com/folders/7KpQmWz3RtYx9LbNc2VdHs4FgJ6aE8uTo?usp=sharing

• Design Inspiration (don't feel limited by this): https://www.layoutboard-demo.com/design/PLKJ8hgFd3S/z9YxW8vU7tS6rQ5pO4nM3L/edit?utm_content=PLKJ8hgFd3S&utm_campaign=designshare&utm_medium=link2&utm_source=sharebutton

______________

The winner will be asked to provide design files and finished PNGs of the overall design file, backgrounds, photo treatments/frames, and icons.

The winner will likely be engaged for a phase 2 to build out a product page.

Industry/Entity Type

Alarm Systems, Home Theatres, and Commercial IT Networking

Number of Pages Required

1 page

Font styles to use
Sans Serif

Colors
0054AA
0677BA
7BADD7
CADEEF
E8F1F8
0094D4
00A9DD
6FCCEA
C7EBF8
E9F6FB
EB3D1F
EC4F4E
F09395
F8D3D4
FCEDEE

Requirements
Must have
• 1. Appeal to both men and women. The logo is a bit masculine, so the colors and icons must soften this. 2. Feel modern - we need to convey that we we use the latest technology. 3. Feel a bit high-end. We are not a budget solution. 4. Have a distinct iconography and photo treatment. 5. Feel layered - not just a series of stacked horizontal modules.
Should not have
• 1. Should not feel like just another IT website.

```html
<!DOCTYPE html>
<html lang="en">
<head>
<meta charset="utf-8">
<title>Brightfern Systems — Safer, Smarter, Faster</title>
<link href="https://fonts.googleapis.com/css2?family=Russo+One&family=Poppins:wght@400;500;600;700&display=swap" rel="stylesheet">
<style>
:root{
  --blue:#1a4fbf;
  --blue-deep:#0054aa;
  --blue-mid:#0677ba;
  --blue-soft:#cadeef;
  --blue-pale:#e8f1f8;
  --sky:#6fccea;
  --red:#eb3d1f;
  --ink:#1b1b1f;
  --muted:#55575e;
  --card:#f2f3f6;
  --white:#ffffff;
  --dark:#1c1f26;
}
*{box-sizing:border-box;margin:0;padding:0}
html,body{width:1200px;height:5216px;overflow:hidden}
body{position:relative;background:var(--white);font-family:"Poppins",sans-serif;color:var(--ink)}
.display{font-family:"Russo One",sans-serif;text-transform:uppercase;letter-spacing:.5px}
.red{color:var(--red)}
.abs{position:absolute}
.btn{position:absolute;display:flex;align-items:center;justify-content:center;font-weight:600;font-size:12px;border-radius:2px}
.btn-blue{background:var(--blue);color:var(--white)}
.btn-white{background:var(--white);color:var(--blue)}

/* header */
.topbar{top:0;left:0;width:1200px;height:77px;background:var(--white)}
.brand{position:absolute;display:flex;align-items:center;gap:8px;font-family:"Russo One",sans-serif;color:var(--blue)}
.brand-mark{width:14px;height:14px;background:var(--red);border-radius:50%}
.header-brand{left:92px;top:10px;width:130px;height:122px;background:var(--white);border-radius:0 0 60px 60px;box-shadow:0 4px 10px rgba(0,0,0,.15);flex-direction:column;justify-content:center;font-size:17px;text-align:center;line-height:1.1;z-index:3}
.topnav{position:absolute;top:33px;left:526px;display:flex;gap:30px;font-size:14px;font-weight:500}
.topicons{position:absolute;top:26px;left:993px;display:flex;gap:34px}
.subnav{top:77px;left:0;width:1200px;height:67px;background:var(--blue);display:flex;gap:48px;padding-left:450px;align-items:center;color:var(--white);font-size:12px;font-weight:700;letter-spacing:.3px}
.subnav span::after{content:" ⌄";font-weight:400}

/* hero */
.hero{top:144px;left:0;width:1200px;height:504px;overflow:hidden}
.hero-photo{position:absolute;inset:0;background:linear-gradient(180deg,#9fb7a0 0%,#6f9a62 35%,#4c7d3f 70%,#355f2d 100%)}
.hero-house{position:absolute;left:640px;top:20px;width:520px;height:360px;border-radius:12px;background:linear-gradient(160deg,#c9d5e2,#7e8fa5 60%,#4d5b70)}
.hero-shade{position:absolute;inset:0;background:linear-gradient(90deg,rgba(20,40,30,.65) 0%,rgba(20,40,30,.2) 45%,rgba(0,0,0,0) 60%)}
.hero-copy{position:absolute;left:51px;top:82px;color:var(--white)}
.hero-kicker{font-size:19px}
.hero-big{font-size:50px;line-height:63px;margin-top:14px}
.hero-sub{font-size:28px;margin-top:14px}

/* intro cards */
.intro-card{position:absolute;top:688px;width:340px;height:368px;background:var(--card);border-radius:6px}
.intro-photo{position:absolute;left:16px;top:24px;width:308px;height:214px;border-radius:6px}
.intro-title{position:absolute;left:18px;font-size:20px;line-height:28px}
.intro-sub{position:absolute;left:18px;font-size:13px;color:var(--muted)}

/* feature section */
.section-title{font-size:38px;line-height:48px}
.feature{position:absolute;width:340px;height:308px;background:var(--card);border-radius:6px;overflow:hidden}
.feature-icon{position:absolute;left:18px;top:22px;width:60px;height:60px;border-radius:50%}
.feature-trace{position:absolute;left:0;bottom:0;width:100%;height:120px;background:linear-gradient(180deg,rgba(202,222,239,0),rgba(202,222,239,.7))}
.feature h3{position:absolute;left:18px;top:92px;font-size:28px;line-height:38px;font-weight:400}
.feature p{position:absolute;left:18px;font-size:13px;line-height:21px;color:var(--muted);width:300px}
.feature-monitor{background:var(--blue)}
.feature-monitor h3{color:var(--white);top:30px}
.feature-monitor p{color:var(--white);top:100px}

/* steps */
.step{position:absolute;top:2120px;width:240px;height:264px;border-radius:28px;display:flex;flex-direction:column;align-items:center;justify-content:center;text-align:center;font-family:"Russo One",sans-serif;text-transform:uppercase}
.step-num{font-size:26px;margin-bottom:18px}
.step-label{font-size:23px;line-height:30px}
.step-desc{position:absolute;top:2414px;width:320px;text-align:center;font-size:14px;line-height:22px;color:var(--ink)}

/* testimonials */
.reviews{top:2611px;left:0;width:1200px;height:486px;background:linear-gradient(135deg,#f7fbfe 0%,#e9f6fb 50%,#f7fbfe 100%)}
.review-card{position:absolute;left:472px;top:51px;width:678px;height:390px;background:var(--white);border-radius:24px;box-shadow:0 6px 24px rgba(0,0,0,.08)}
.avatar{position:absolute;border-radius:50%;background:linear-gradient(160deg,#d9dde4,#8d96a6)}
.reviewer{position:absolute;font-size:14px;line-height:24px}
.reviewer b{font-weight:600}
.arrow{position:absolute;width:36px;height:36px;border-radius:50%;background:var(--blue-pale);display:flex;align-items:center;justify-content:center}

/* partners */
.partners{top:3202px;left:0;width:1200px;height:136px;background:var(--blue);display:flex;align-items:center;justify-content:space-around;color:var(--white);font-family:"Russo One",sans-serif;font-size:34px;padding:0 10px}

/* founder */
.founder{top:3400px;left:40px;width:1104px;height:512px;border-radius:26px;overflow:hidden;background:var(--dark)}
.founder-scene{position:absolute;inset:0;background:linear-gradient(90deg,#15181e 0%,#2a2f38 45%,#3d434d 70%,#22262d 100%)}
.founder-portrait{position:absolute;right:110px;top:22px;width:310px;height:490px;border-radius:140px 140px 0 0;background:linear-gradient(180deg,#4a5566,#2f3744 60%,#1d222b)}
.founder h2{position:absolute;left:24px;top:48px;color:var(--white);font-size:35px;line-height:48px;font-weight:400;width:620px}
.founder ul{position:absolute;left:44px;top:272px;width:440px;color:var(--white);font-size:13.5px;line-height:22px}
.badge{top:3831px;left:587px;width:213px;height:213px;border-radius:50%;background:var(--white);box-shadow:0 4px 14px rgba(0,0,0,.15);display:flex;align-items:center;justify-content:center;text-align:center;z-index:2}
.signature{top:3916px;left:830px;width:273px;height:122px;border-radius:8px;background:linear-gradient(90deg,rgba(26,79,191,.06),rgba(26,79,191,.12))}

/* quote */
.quote{top:4074px;left:0;width:1200px;height:581px;overflow:hidden}
.quote-photo{position:absolute;inset:0;background:linear-gradient(90deg,#8a6a2a 0%,#b08a3e 18%,#5b5446 45%,#2f2f33 70%,#1e1e22 100%)}
.quote-shade{position:absolute;inset:0;background:rgba(0,0,0,.35)}
.field{position:absolute;background:var(--white);border-radius:3px;font-size:11px;color:#8b8d93;padding:12px 14px}

/* newsletter */
.newsletter{top:4655px;left:0;width:1200px;height:215px;background:var(--blue)}

/* footer */
.footer{top:4870px;left:0;width:1200px;height:346px;background:var(--white)}
.fcol{position:absolute;top:74px;font-size:14px;line-height:28px}
.fcol h4{font-size:13px;font-weight:700;margin-bottom:8px;letter-spacing:.3px}
</style>
</head>
<body>

<header>
  <div class="abs topbar">
    <div class="brand header-brand"><span class="brand-mark"></span>Brightfern<br>Systems</div>
    <nav class="topnav"><span>Home</span><span>About</span><span>Project Consulting</span><span>Contact Us</span></nav>
    <div class="topicons">
      <svg width="26" height="26" viewBox="0 0 26 26" aria-label="Search"><circle cx="11" cy="11" r="7.5" fill="none" stroke="#1a4fbf" stroke-width="3"/><line x1="16.5" y1="16.5" x2="23" y2="23" stroke="#1a4fbf" stroke-width="3" stroke-linecap="round"/></svg>
      <svg width="24" height="24" aria-label="Social profile"><circle cx="12" cy="12" r="11" fill="#1a4fbf"/></svg>
      <svg width="24" height="24" aria-label="Social profile"><rect x="1" y="1" width="22" height="22" rx="3" fill="#1a4fbf"/></svg>
    </div>
  </div>
  <nav class="abs subnav"><span>AUDIO + VIDEO</span><span>ELECTRONIC SECURITY</span><span>NETWORKING + COMMUNICATION</span><span>CABLING</span></nav>
</header>

<section class="abs hero">
  <div class="hero-photo" role="img" aria-label="Green rolling hills of Middle Tennessee with a modern two-storey home lit at dusk"></div>
  <div class="hero-house" role="img" aria-label="Modern home with glowing windows"></div>
  <div class="hero-shade"></div>
  <svg class="abs" style="left:0;top:0" width="1200" height="504" viewBox="0 0 1200 504"><path d="M0 370 C300 420 700 480 1200 452 L1200 504 L0 504 Z" fill="#1a4fbf"/><path d="M0 372 C300 422 700 482 1200 454" fill="none" stroke="#6fccea" stroke-width="3" opacity=".7"/></svg>
  <div class="hero-copy">
    <div class="display hero-kicker">Proudly Serving Middle Tennessee</div>
    <div class="display hero-big">Safer<span class="red">.</span><br>Smarter<span class="red">.</span><br>Faster<span class="red">.</span></div>
    <div class="display hero-sub">Homes <span class="red">+</span> Businesses</div>
  </div>
</section>

<section>
  <article class="intro-card" style="left:61px">
    <div class="intro-photo" style="background:linear-gradient(150deg,#c9a98a,#6d6f78 55%,#2d3340)" role="img" aria-label="Team on a video conference call in a meeting room"></div>
    <h3 class="display intro-title" style="top:272px">Affordable Security</h3>
    <p class="intro-sub" style="top:310px">For Homes • For Businesses</p>
  </article>
  <article class="intro-card" style="left:429px">
    <div class="intro-photo" style="background:linear-gradient(180deg,#3a4250,#1d222b 70%,#11141a)" role="img" aria-label="Large modern house at night with lit windows"></div>
    <h3 class="display intro-title" style="top:268px">Enviable<br>Entertainment</h3>
    <p class="intro-sub" style="top:334px">For Homes • For Businesses</p>
  </article>
  <article class="intro-card" style="left:800px">
    <div class="intro-photo" style="background:linear-gradient(150deg,#e6e1da,#c8b7a0 50%,#8c6a4d)" role="img" aria-label="Person arming a wall-mounted security keypad"></div>
    <h3 class="display intro-title" style="top:268px">Connected<br>Businesses</h3>
    <p class="intro-sub" style="top:334px">For Homes • For Businesses</p>
  </article>
</section>

<section>
  <h2 class="abs display section-title" style="left:61px;top:1110px">Connect <span class="red">+</span> Protect Your<br>World</h2>
  <p class="abs" style="left:61px;top:1220px;width:260px;font-size:13.5px;line-height:22px">Protect your people, assets, and information from whatever comes.</p>

  <article class="feature" style="left:61px;top:1297px">
    <div class="feature-trace"></div>
    <div class="feature-icon" style="background:linear-gradient(150deg,#e8f1f8,#7badd7)" role="img" aria-label="Entry and motion sensor icon"></div>
    <h3 class="display">Entry <span class="red">&amp;</span> Motion<br>Sensors</h3>
    <p style="top:184px">Pair text with an icon to focus on your chosen product, collection, or blog post.</p>
  </article>
  <article class="feature" style="left:429px;top:1297px">
    <div class="feature-trace"></div>
    <div class="feature-icon" style="background:linear-gradient(150deg,#c7ebf8,#0094d4)" role="img" aria-label="Video doorbell icon"></div>
    <h3 class="display">Video<br>Doorbells</h3>
    <p style="top:184px">Pair text with an icon to focus on your chosen product, collection, or blog post.</p>
  </article>
  <article class="feature" style="left:800px;top:1297px">
    <div class="feature-trace"></div>
    <div class="feature-icon" style="background:linear-gradient(150deg,#cadeef,#0054aa)" role="img" aria-label="Security camera icon"></div>
    <h3 class="display">Security<br>Cameras</h3>
    <p style="top:184px">Pair text with an icon to focus on your chosen product, collection, or blog post.</p>
  </article>
  <article class="feature" style="left:61px;top:1635px">
    <div class="feature-trace"></div>
    <div class="feature-icon" style="background:linear-gradient(150deg,#fcedee,#ec4f4e)" role="img" aria-label="Pet-friendly paw icon"></div>
    <h3 class="display" style="top:92px">Pet <span class="red">–</span> Friendly</h3>
    <p style="top:146px">Pair text with an icon to focus on your chosen product, collection, or blog post.</p>
  </article>
  <article class="feature" style="left:429px;top:1635px">
    <div class="feature-trace"></div>
    <div class="feature-icon" style="background:linear-gradient(150deg,#e9f6fb,#00a9dd)" role="img" aria-label="Fire and carbon monoxide detector icon"></div>
    <h3 class="display">Fire <span class="red">&amp;</span> Carbon<br>Monoxide</h3>
    <p style="top:184px">Pair text with an icon to focus on your chosen product, collection, or blog post.</p>
  </article>
  <article class="feature feature-monitor" style="left:800px;top:1635px">
    <h3 class="display">24<span class="red">/</span>7 Monitoring</h3>
    <p>Our team is always on guard. With always-on protection, we’ll notify you of any suspicious activity. In emergencies, we’ll monitor your local police, fire, or EMS.</p>
    <div class="btn btn-white" style="left:18px;top:244px;width:122px;height:30px;font-size:11px">ORDER NOW</div>
  </article>
</section>

<section>
  <h2 class="abs display section-title" style="left:0;top:2002px;width:1200px;text-align:center;font-size:35px">A Safer Home or Business is as<br>Easy as 1<span class="red">–</span>2<span class="red">–</span>3</h2>

  <div class="step" style="left:127px;background:linear-gradient(160deg,#fcedee,#f8d3d4);color:#e23a27" role="img" aria-label="Red shield badge illustration for step one">
    <span class="step-num">01</span><span class="step-label">Build an<br>Instant<br>Quote</span>
  </div>
  <div class="step" style="left:480px;background:linear-gradient(160deg,#e8f1f8,#cadeef);color:var(--blue)" role="img" aria-label="Blue shield badge illustration for step two">
    <span class="step-num">02</span><span class="step-label">Schedule<br>Installation</span>
  </div>
  <div class="step" style="left:833px;background:linear-gradient(160deg,#f2f3f6,#d8dadf);color:#2a2c31" role="img" aria-label="Dark shield badge illustration for step three">
    <span class="step-num">03</span><span class="step-label">Stay<br>Secure<br>24/7</span>
  </div>

  <p class="step-desc" style="left:87px">Our live-estimate builder will guide you through a few questions to help us understand your needs.</p>
  <p class="step-desc" style="left:440px">Our trained techs are efficient and friendly. Southern-born and raised (and one mid-westerner), we will respect your home and your schedule.</p>
  <p class="step-desc" style="left:793px">Monitor your home through the app, receive instant alerts, and rely on professional monitoring services for emergencies.</p>

  <div class="btn btn-blue" style="left:184px;top:2520px;width:126px;height:28px">Get Started</div>
  <div class="btn btn-blue" style="left:537px;top:2520px;width:126px;height:28px">Get Started</div>
  <div class="btn btn-blue" style="left:890px;top:2520px;width:126px;height:28px">Get Started</div>
</section>

<section class="abs reviews">
  <h2 class="abs display section-title" style="left:61px;top:44px;font-size:37px">Hear What Our<br>Clients Have To<br>Say.</h2>
  <div class="abs display" style="left:61px;top:206px;width:172px;height:170px;background:var(--blue);color:var(--white);font-size:22px;line-height:32px;padding:40px 8px 0">(300+)<br>Customer<br>Reviews</div>

  <div class="review-card">
    <div class="avatar" style="left:30px;top:36px;width:204px;height:204px" role="img" aria-label="Portrait of reviewer Dana Whitfield"></div>
    <p class="abs" style="left:267px;top:30px;width:376px;font-size:13.5px;line-height:22px">Fantastic service!! Used SafeLine and HomeGuardian in the past, and their customer service does not compare to Brightfern! Installation and set up went smoothly!! It’s so convenient to use the apps remotely for the cameras, and arming or unarming the alarm. I’d rate them more than 5 stars if I was able to!</p>
    <div class="reviewer" style="left:267px;top:198px"><b>Dana Whitfield</b><br>Trust Office</div>
    <div class="abs" style="left:556px;top:198px;color:#f5a623;font-size:18px;letter-spacing:2px">★★★★</div>
    <svg class="abs" style="left:586px;top:224px" width="50" height="24"><circle cx="11" cy="12" r="10" fill="#1a4fbf"/><rect x="28" y="2" width="20" height="20" rx="3" fill="#1a4fbf"/></svg>
    <div class="avatar" style="left:48px;top:268px;width:74px;height:74px" role="img" aria-label="Portrait of reviewer"></div>
    <div class="reviewer" style="left:130px;top:278px"><b>Dana Whitfield</b><br>Trust Office</div>
    <div class="avatar" style="left:362px;top:268px;width:74px;height:74px" role="img" aria-label="Portrait of reviewer"></div>
    <div class="reviewer" style="left:444px;top:278px"><b>Dana Whitfield</b><br>Trust Office</div>
    <div class="arrow" style="left:560px;top:340px"><svg width="14" height="14"><path d="M9 2 L4 7 L9 12" fill="none" stroke="#1a4fbf" stroke-width="2"/></svg></div>
    <div class="arrow" style="left:609px;top:340px"><svg width="14" height="14"><path d="M5 2 L10 7 L5 12" fill="none" stroke="#1a4fbf" stroke-width="2"/></svg></div>
  </div>
</section>

<h2 class="abs display section-title" style="left:0;top:3124px;width:1200px;text-align:center;font-size:34px">Service Partners</h2>
<section class="abs partners">
  <span>Corvane</span><span>Lockwell</span><span>Veridian</span><span>Optiscope</span><span>Talvero</span>
</section>

<section class="abs founder">
  <div class="founder-scene" role="img" aria-label="Dusk view of a large home behind the company founder"></div>
  <div class="founder-portrait" role="img" aria-label="Founder Holden Ashby in a blue suit and bow tie"></div>
  <h2 class="display">I Founded Brightfern Systems to Bring Together Technology and Honest, Reliable Service.</h2>
  <ul>
    <li>I’m proud to call Tennessee home and even prouder to help keep its homes and businesses secure.</li>
    <li>Whether it’s protecting or elevating your space, my goal is to make technology work for you.</li>
    <li>Think of us as your friendly, neighborhood tech expert—here to safeguard what matters most.</li>
  </ul>
  <div class="btn btn-blue" style="left:32px;top:435px;width:176px;height:28px;font-size:11px">Tell Us How We Can Help</div>
  <div class="btn btn-white" style="left:226px;top:435px;width:90px;height:28px;font-size:11px">About Us</div>
</section>
<div class="abs badge"><div class="brand" style="position:static;flex-direction:column;font-size:20px;line-height:1.15"><span class="brand-mark"></span>Brightfern<br>Systems</div></div>
<div class="abs signature" role="img" aria-label="Handwritten signature of Holden Ashby"></div>

<section class="abs quote">
  <div class="quote-photo" role="img" aria-label="Child running at sunset beside a dim modern interior"></div>
  <div class="quote-shade"></div>
  <h2 class="abs display" style="left:0;top:62px;width:1200px;text-align:center;color:var(--white);font-size:46px">Request A Quote</h2>
  <p class="abs" style="left:0;top:126px;width:1200px;text-align:center;color:var(--white);font-size:13px">If You Have Question, Please Use Our 24-7 Hours Helpline</p>
  <div class="field" style="left:259px;top:190px;width:322px;height:41px">First Name *</div>
  <div class="field" style="left:613px;top:190px;width:322px;height:41px">Last Name *</div>
  <div class="field" style="left:259px;top:263px;width:322px;height:41px">Email *</div>
  <div class="field" style="left:613px;top:263px;width:322px;height:41px">Select Option</div>
  <div class="field" style="left:259px;top:338px;width:676px;height:102px">Write Your detail Heres...</div>
  <div class="btn btn-blue" style="left:538px;top:474px;width:124px;height:32px">Submit</div>
</section>

<section class="abs newsletter">
  <h2 class="abs display" style="left:55px;top:36px;color:var(--white);font-size:35px;line-height:50px">Subscribe To Our<br>Newsletter</h2>
  <p class="abs" style="left:55px;top:152px;color:var(--white);font-size:14px;font-weight:600">Security Tips, Special Offers, and More!</p>
  <div class="field" style="left:826px;top:67px;width:348px;height:35px;color:#3a3c42;padding:9px 10px">Your Mail</div>
  <div class="btn" style="left:826px;top:118px;width:121px;height:32px;background:#0677ba;color:var(--white)">Sign UP</div>
</section>

<footer class="abs footer">
  <div class="brand" style="left:81px;top:106px;font-size:28px;line-height:1.1"><span class="brand-mark"></span>Brightfern<br>Systems</div>
  <div class="fcol" style="left:385px"><h4>COMMERCIAL</h4>Audio Video<br>Cabling<br>Communication<br>Electronic Security<br>Project Consulting</div>
  <div class="fcol" style="left:642px;top:68px"><h4>RESIDENTIAL</h4>Home Security<br>Smart Homes<br>Home Theatres + A/V<br>WiFi<br>Cabling</div>
  <div class="fcol" style="left:907px;top:68px;width:230px;font-size:13.5px;line-height:24px"><h4>PROUDLY SERVING MIDDLE TENNESSEE</h4>482 Summit Ridge Rd. Suite 2-210<br>Hendersonville, TN 37075<br><div style="margin-top:10px">615.555.0142</div><div style="margin-top:6px">Request A Quote</div>
    <svg width="96" height="16" style="margin-top:4px"><circle cx="8" cy="8" r="7" fill="#1b1b1f"/><rect x="24" y="1" width="14" height="14" rx="3" fill="#1b1b1f"/><rect x="48" y="2" width="16" height="12" rx="3" fill="#1b1b1f"/><path d="M74 2 L86 14 M86 2 L74 14" stroke="#1b1b1f" stroke-width="2"/></svg>
  </div>
  <div class="abs" style="left:61px;top:287px;width:1130px;height:1px;background:#c9cbd0"></div>
  <p class="abs" style="left:0;top:309px;width:1200px;text-align:center;font-size:13px;word-spacing:2px">© 2024 Brightfern Systems. All Rights Reserved. &nbsp;&nbsp;&nbsp; Terms &amp; Conditions &nbsp;&nbsp;&nbsp; Privacy Policy</p>
</footer>

</body>
</html>
```